BrindleQuartos

We need a book cover for an upcoming book publication. Please see attachment for the text that should go on the book cover. We want a sleek and impacting design, but not overly busy. The target industry is oral-maxillofacial. Thanks and good luck!

```html
<!DOCTYPE html>
<html lang="en">
<head>
<meta charset="UTF-8">
<title>BrindleQuartos — Book Cover</title>
<link rel="stylesheet" href="https://fonts.googleapis.com/css2?family=Roboto+Condensed:wght@400;700&display=swap">
<style>
  :root {
    --backdrop: #eee8df;
    --cover-top: #6f6e93;
    --cover-mid: #5d5a7e;
    --cover-low: #524e70;
    --cover-glow: #8a7285;
    --ink-light: #ffffff;
    --ink-soft: #e6e4f0;
    --rule: rgba(255, 255, 255, 0.85);
    --author-band: rgba(255, 255, 255, 0.08);
    --photo-warm: #f3d9d6;
    --photo-cool: #dde8f0;
    --photo-pale: #eef3f6;
  }

  * { box-sizing: border-box; margin: 0; padding: 0; }

  html, body {
    width: 1200px;
    height: 1000px;
    overflow: hidden;
    background: var(--backdrop);
  }

  .canvas {
    position: relative;
    width: 1200px;
    height: 1000px;
    display: flex;
    align-items: center;
    justify-content: center;
  }

  .book-cover {
    position: relative;
    width: 376px;
    height: 946px;
    overflow: hidden;
    font-family: "Roboto Condensed", "Arial Narrow", sans-serif;
    color: var(--ink-light);
    background:
      radial-gradient(ellipse 55% 22% at 75% 92%, var(--cover-glow) 0%, transparent 100%),
      linear-gradient(180deg, var(--cover-top) 0%, var(--cover-mid) 45%, var(--cover-low) 100%);
  }

  .book-cover::before {
    content: "";
    position: absolute;
    left: 10px;
    top: 0;
    bottom: 0;
    width: 2px;
    background: rgba(0, 0, 0, 0.12);
  }

  .cover-title {
    position: absolute;
    top: 156px;
    left: 24px;
    right: 16px;
    text-align: right;
    white-space: nowrap;
    font-size: 39px;
    font-weight: 700;
    letter-spacing: 0;
    line-height: 1;
  }

  .author-band {
    position: absolute;
    top: 290px;
    left: 0;
    width: 100%;
    height: 48px;
    border-top: 2px solid var(--rule);
    background: var(--author-band);
  }

  .author-name {
    position: absolute;
    right: 14px;
    top: 16px;
    font-size: 13px;
    font-weight: 400;
    color: var(--ink-soft);
    white-space: nowrap;
  }

  .cover-photo {
    position: absolute;
    top: 338px;
    left: 0;
    width: 100%;
    height: 285px;
    background:
      linear-gradient(90deg, var(--photo-warm) 0%, var(--photo-warm) 22%, var(--photo-cool) 40%, var(--photo-pale) 100%);
  }

  .definition {
    position: absolute;
    top: 664px;
    left: 40px;
    right: 12px;
    font-size: 12px;
    line-height: 1.4;
  }

  .definition-head {
    margin-bottom: 22px;
    letter-spacing: 0.3px;
  }

  .definition-list {
    list-style: none;
  }

  .definition-item {
    display: flex;
    gap: 12px;
    margin-bottom: 16px;
  }

  .definition-num {
    flex: none;
    width: 14px;
  }

  .definition-text--single {
    white-space: nowrap;
  }
</style>
</head>
<body>
  <main class="canvas">
    <article class="book-cover">
      <h1 class="cover-title">BRINDLEQUARTOS</h1>

      <div class="author-band">
        <p class="author-name">Name of the author</p>
      </div>

      <div class="cover-photo" role="img" aria-label="Close-up photograph of a bright, healthy smile against a soft pale blue background"></div>

      <section class="definition">
        <p class="definition-head">noun &nbsp;|&nbsp; \ brin - dl - \ kwor - tōs</p>
        <ol class="definition-list">
          <li class="definition-item"><span class="definition-num">1 :</span><span class="definition-text--single">the practice of clinical aesthetics with medical-grade products.</span></li>
          <li class="definition-item"><span class="definition-num">2 :</span><span>a universal clinical perception of natural geometric forms<br>and height of contours.</span></li>
          <li class="definition-item"><span class="definition-num">3 :</span><span>aesthetic diagnosis and treatment knowledgebase.</span></li>
        </ol>
      </section>
    </article>
  </main>
</body>
</html>
```